Webpage Needed for Bright Harbor Wiring Electrical and Security

We need a web design for our company showing people we arent just a small business. We want to look big so people can trust us. I would like information from my business cards on the page. example, we do all house rennovations, construction, commercial, 24 hour emergency service, new installations, repairs, maintenance, home theatre and so on...

I would also like images from my facebook on the page and linked. facebook.com/brightharborwiring

Target Market(s)

builders, residents,

Industry/Entity Type

Business

Number of Pages Required

1 page

Font styles to use
Other font styles liked:
• Juice bold

Requirements
Must have
• colours the same as the logo. background must be white. also the font must be Juice Bold which is the font of the logo
Should not have
• black as the background

```html
<!DOCTYPE html>
<html lang="en">
<head>
<meta charset="utf-8">
<title>Bright Harbor Wiring Electrical and Security</title>
<link href="https://fonts.googleapis.com/css2?family=Exo+2:wght@400;600;700&family=Open+Sans:wght@400;600;700&display=swap" rel="stylesheet">
<style>
:root{
  --orange:#f7941d;
  --orange-deep:#f26f21;
  --blue:#1fa3dc;
  --ink:#2d3035;
  --text:#6b6b6b;
  --muted:#9a9a9a;
  --line:#e4e4e4;
  --hero:#efe8df;
  --concrete:#d9d9d9;
  --gallery:#121212;
  --white:#ffffff;
  --logo-band:#f1f1f1;
  --footer:#2b2f34;
}
*{box-sizing:border-box;margin:0;padding:0}
html,body{width:1200px;height:3313px;overflow:hidden}
body{background:var(--white);font-family:"Open Sans",Arial,sans-serif;color:var(--text);position:relative}
.display{font-family:"Exo 2",Arial,sans-serif}
.abs{position:absolute}

/* header */
.site-header{position:absolute;left:0;top:0;width:1200px;height:155px;background:var(--white)}
.topbar{position:absolute;right:70px;top:14px;font-size:12px;color:var(--muted);display:flex;gap:26px;align-items:center}
.topbar-social{position:absolute;left:104px;top:12px;display:flex;gap:8px}
.topbar-social span{width:14px;height:14px;border-radius:50%;background:#c9c9c9;display:block}
.brand{position:absolute;left:100px;top:48px;display:flex;align-items:center;gap:12px}
.brand-mark{width:30px;height:30px;border-radius:50%;background:var(--orange)}
.brand-name{font-family:"Exo 2",Arial,sans-serif;font-weight:700;font-size:22px;line-height:1.05;color:var(--ink);width:170px}
.main-nav{position:absolute;right:70px;top:92px;display:flex;gap:30px;font-size:12px;font-weight:700;color:var(--ink);letter-spacing:.5px}
.main-nav .active{color:var(--orange)}
.header-rule{position:absolute;left:0;top:154px;width:1200px;height:1px;background:var(--line)}

/* hero */
.hero{position:absolute;left:0;top:155px;width:1200px;height:507px;background:linear-gradient(90deg,#f3efe9 0%,var(--hero) 55%,#e7ddd0 100%)}
.hero-photo{position:absolute;left:520px;top:0;width:680px;height:507px;background:radial-gradient(ellipse at 40% 45%,#e9c9a8 0%,#d9c3ab 30%,rgba(231,221,208,0) 70%)}
.hero-title{position:absolute;left:100px;top:70px;font-family:"Exo 2",Arial,sans-serif;font-weight:600;font-size:82px;line-height:1;color:var(--orange)}
.hero-sub{position:absolute;left:100px;top:276px;background:var(--white);padding:12px 18px;font-size:12px;font-weight:600;color:var(--ink);letter-spacing:.3px}
.btn-dark{position:absolute;left:100px;top:353px;background:var(--ink);color:var(--white);font-size:12px;font-weight:700;padding:10px 18px;letter-spacing:.5px;display:flex;gap:12px;align-items:center}

/* about */
.about-photo{position:absolute;left:74px;top:715px;width:312px;height:350px;background:radial-gradient(ellipse at 50% 50%,#c9a58b 0%,#e5d5c7 45%,#ffffff 75%)}
.about-title{position:absolute;left:442px;top:820px;font-family:"Exo 2",Arial,sans-serif;color:var(--ink)}
.about-title strong{display:block;font-size:32px;font-weight:700}
.about-title span{display:block;font-size:30px;font-weight:400}
.about-text{position:absolute;left:442px;top:925px;width:660px;font-size:13px;line-height:1.7}
.btn-outline{position:absolute;left:442px;top:1010px;border:2px solid var(--orange);color:var(--orange);font-size:12px;font-weight:700;padding:9px 16px;letter-spacing:.5px}

/* features */
.features-rule{position:absolute;left:100px;top:1130px;width:1000px;height:1px;background:var(--line)}
.feature{position:absolute;top:1172px;width:300px}
.feature svg{position:absolute;left:0;top:0}
.feature h3{position:absolute;left:54px;top:2px;font-family:"Exo 2",Arial,sans-serif;font-size:22px;font-weight:600;color:var(--ink);white-space:nowrap}
.feature p{position:absolute;left:54px;top:38px;width:240px;font-size:12px;line-height:1.6}

/* services */
.services{position:absolute;left:0;top:1325px;width:1200px;height:478px;background:radial-gradient(circle at 20% 30%,#e4e4e4 0%,var(--concrete) 60%,#cfcfcf 100%)}
.section-title{position:absolute;left:0;width:1200px;text-align:center;font-family:"Exo 2",Arial,sans-serif;font-weight:700;font-size:38px;letter-spacing:2px}
.services .section-title{top:40px;color:var(--orange)}
.service{position:absolute;top:130px;width:190px;text-align:center}
.service .icon{width:86px;height:86px;border-radius:50%;background:var(--orange);margin:0 auto;display:flex;align-items:center;justify-content:center}
.service h4{margin-top:20px;font-family:"Exo 2",Arial,sans-serif;font-size:17px;font-weight:600;color:var(--ink)}
.service p{margin-top:8px;font-size:12px;line-height:1.55;color:#555}
.service .more{display:block;margin-top:14px;font-size:12px;color:var(--orange);font-weight:600}
.btn-list{position:absolute;left:505px;top:406px;width:190px;border:2px solid var(--ink);color:var(--ink);font-size:11px;font-weight:700;text-align:center;padding:8px 0;letter-spacing:.5px}

/* gallery */
.gallery{position:absolute;left:0;top:1803px;width:1200px;height:737px;background:var(--gallery)}
.gallery .section-title{top:40px;color:var(--white)}
.filters{position:absolute;left:145px;top:106px;display:flex;gap:22px;font-size:11px;color:#8a8a8a;letter-spacing:.5px}
.filters .active{color:var(--orange);font-weight:700}
.grid{position:absolute;left:0;top:160px;width:1200px;height:472px;display:grid;grid-template-columns:repeat(4,300px);grid-template-rows:repeat(2,236px)}
.tile{background:linear-gradient(160deg,#a7b4bd 0%,#6f7a80 45%,#3a3f42 100%);border:1px solid #1b1b1b}
.tile-feature{background:var(--orange);padding:30px 26px;color:var(--white)}
.tile-feature h5{font-family:"Exo 2",Arial,sans-serif;font-size:22px;font-weight:700}
.tile-feature p{margin-top:12px;border:1px solid rgba(255,255,255,.8);padding:8px 10px;font-size:11px;line-height:1.5}
.btn-orange{position:absolute;left:512px;top:667px;width:176px;background:var(--orange);color:var(--white);font-size:11px;font-weight:700;text-align:center;padding:9px 0;letter-spacing:.5px}

/* testimonials */
.testimonials{position:absolute;left:0;top:2540px;width:1200px;height:435px;background:linear-gradient(90deg,var(--orange) 0%,#f9a43a 55%,var(--orange-deep) 100%)}
.testimonials-photo{position:absolute;right:0;top:0;width:520px;height:435px;background:radial-gradient(ellipse at 60% 50%,rgba(255,214,160,.7) 0%,rgba(247,148,29,0) 70%)}
.testimonials .section-title{top:50px;color:var(--white)}
.avatar{position:absolute;left:568px;top:148px;width:64px;height:64px;border-radius:50%;background:#f3d3b0;border:3px solid var(--white)}
.client{position:absolute;left:0;top:238px;width:1200px;text-align:center;font-size:12px;font-weight:700;color:var(--white);letter-spacing:.5px}
.quote{position:absolute;left:200px;top:292px;width:800px;text-align:center;font-size:12px;line-height:1.7;color:var(--white)}
.dots{position:absolute;left:570px;top:380px;display:flex;gap:8px}
.dots span{width:14px;height:14px;border-radius:50%;background:var(--white);opacity:.6}
.dots span.on{opacity:1}

/* partner logos */
.partners{position:absolute;left:0;top:2975px;width:1200px;height:153px;background:var(--logo-band);display:flex;justify-content:center;align-items:center;gap:80px}
.partner{display:flex;align-items:center;gap:8px;font-size:12px;font-weight:700;color:#b3b3b3;letter-spacing:1px}
.partner i{width:20px;height:20px;background:#c8c8c8;display:block}

/* footer */
.site-footer{position:absolute;left:0;top:3128px;width:1200px;height:185px;background:var(--footer)}
.footer-contact{position:absolute;left:100px;top:62px;font-size:11px;line-height:2;color:#8e949b;letter-spacing:.4px}
.footer-brand{position:absolute;left:500px;top:56px;width:200px;display:flex;align-items:center;gap:10px}
.footer-brand .brand-mark{width:26px;height:26px}
.footer-brand .brand-name{color:var(--white);font-size:19px;width:160px}
.footer-legal{position:absolute;right:100px;top:62px;font-size:11px;color:var(--orange);font-weight:700;letter-spacing:.4px}
.footer-legal span{color:#8e949b;font-weight:400}
.footer-social{position:absolute;right:100px;top:100px;display:flex;gap:10px}
.footer-social span{width:26px;height:26px;border-radius:50%;border:1px solid #6f757c;display:block}
</style>
</head>
<body>

<header class="site-header">
  <div class="topbar-social"><span></span><span></span><span></span><span></span></div>
  <div class="topbar"><span>PH: (555) 014-2290</span><span>FAX: (555) 014-2291</span><span>info@brightharborwiring.com</span></div>
  <div class="brand"><span class="brand-mark"></span><span class="brand-name">Bright Harbor Wiring</span></div>
  <nav class="main-nav">
    <span class="active">HOME</span><span>PROJECTS</span><span>WHAT WE DO</span><span>ABOUT US</span><span>BLOG</span><span>SHOP</span><span>CONTACT US</span>
  </nav>
  <div class="header-rule"></div>
</header>

<section class="hero">
  <div class="hero-photo" role="img" aria-label="Photo of a smiling tradeswoman holding a cordless drill"></div>
  <h1 class="hero-title">Just to<br>Satisfy You</h1>
  <p class="hero-sub">NEQUE PORRO QUISQUAM EST QUI DOLOREM IPSUM QUIA</p>
  <div class="btn-dark"><span>GET A FREE QUOTE</span><span>»</span></div>
</section>

<section class="about">
  <div class="about-photo" role="img" aria-label="Photo of a smiling electrician in a yellow hard hat"></div>
  <h2 class="about-title"><strong>25 Years of Experience</strong><span>in Home Maintenance Business</span></h2>
  <p class="about-text">Lorem ipsum dolor sit amet, consectetur adipiscing elit. Quisque nec erat sit amet. Integer blandit, nulla quis fermentum vestibulum, nisi diam viverra metus, porta posuere augue lectus et sapien. Curabitur nec leo quis felis volutpat aliquam et et lacus. Sed varius felis, euismod id euismod at.</p>
  <div class="btn-outline">LET'S GET THE JOB DONE</div>
</section>

<div class="features-rule"></div>
<div class="feature" style="left:100px">
  <svg width="36" height="36" viewBox="0 0 36 36" fill="none" stroke="#f7941d" stroke-width="2"><rect x="6" y="3" width="24" height="30" rx="2"/><line x1="11" y1="11" x2="25" y2="11"/><line x1="11" y1="17" x2="25" y2="17"/><circle cx="18" cy="25" r="3"/></svg>
  <h3>Certification</h3>
  <p>Lorem ipsum dolor sit amet, consectetur adipiscing elit. Quisque nec erat.</p>
</div>
<div class="feature" style="left:440px">
  <svg width="36" height="36" viewBox="0 0 36 36" fill="none" stroke="#f7941d" stroke-width="2"><circle cx="18" cy="18" r="14"/><polyline points="18,9 18,18 24,22"/></svg>
  <h3>24/7 Availability</h3>
  <p>Lorem ipsum dolor sit amet, consectetur adipiscing elit. Quisque nec erat.</p>
</div>
<div class="feature" style="left:780px">
  <svg width="36" height="36" viewBox="0 0 36 36" fill="none" stroke="#f7941d" stroke-width="2"><rect x="4" y="9" width="28" height="20" rx="2"/><line x1="4" y1="15" x2="32" y2="15"/><line x1="9" y1="23" x2="17" y2="23"/></svg>
  <h3>Fair Prices</h3>
  <p>Lorem ipsum dolor sit amet, consectetur adipiscing elit. Quisque nec erat.</p>
</div>

<section class="services">
  <h2 class="section-title">OUR SERVICES</h2>
  <div class="service" style="left:100px">
    <div class="icon"><svg width="44" height="44" viewBox="0 0 44 44" fill="none" stroke="#fff" stroke-width="3"><polyline points="6,22 22,8 38,22"/><rect x="12" y="20" width="20" height="16"/></svg></div>
    <h4>House Renovations</h4>
    <p>Rerum est neque quam libero gravida quam, feugiat augue mollis.</p>
    <span class="more">More »</span>
  </div>
  <div class="service" style="left:305px">
    <div class="icon"><svg width="44" height="44" viewBox="0 0 44 44" fill="none" stroke="#fff" stroke-width="3"><path d="M8 30 a14 14 0 0 1 28 0"/><line x1="5" y1="30" x2="39" y2="30"/><line x1="22" y1="16" x2="22" y2="22"/></svg></div>
    <h4>Construction</h4>
    <p>Rerum est neque quam libero gravida quam, feugiat augue mollis.</p>
    <span class="more">More »</span>
  </div>
  <div class="service" style="left:505px">
    <div class="icon"><svg width="44" height="44" viewBox="0 0 44 44" fill="none" stroke="#fff" stroke-width="3"><rect x="12" y="6" width="20" height="32"/><line x1="17" y1="13" x2="27" y2="13"/><line x1="17" y1="20" x2="27" y2="20"/><line x1="17" y1="27" x2="27" y2="27"/></svg></div>
    <h4>Commercial</h4>
    <p>Rerum est neque quam libero gravida quam, feugiat augue mollis.</p>
    <span class="more">More »</span>
  </div>
  <div class="service" style="left:705px">
    <div class="icon"><svg width="44" height="44" viewBox="0 0 44 44" fill="none" stroke="#fff" stroke-width="3"><rect x="13" y="14" width="18" height="14" rx="3"/><line x1="18" y1="6" x2="18" y2="14"/><line x1="26" y1="6" x2="26" y2="14"/><line x1="22" y1="28" x2="22" y2="38"/></svg></div>
    <h4>New Installations</h4>
    <p>Rerum est neque quam libero gravida quam, feugiat augue mollis.</p>
    <span class="more">More »</span>
  </div>
  <div class="service" style="left:910px">
    <div class="icon"><svg width="44" height="44" viewBox="0 0 44 44" fill="none" stroke="#fff" stroke-width="3"><line x1="10" y1="34" x2="26" y2="18"/><circle cx="30" cy="14" r="7"/><line x1="10" y1="10" x2="34" y2="34"/></svg></div>
    <h4>Maintenance</h4>
    <p>Rerum est neque quam libero gravida quam, feugiat augue mollis.</p>
    <span class="more">More »</span>
  </div>
  <div class="btn-list">PLEASE LIST OF SERVICES »</div>
</section>

<section class="gallery">
  <h2 class="section-title">PROJECT GALLERY</h2>
  <div class="filters">
    <span class="active">ALL</span><span>HOUSE RENOVATIONS</span><span>CONSTRUCTION</span><span>24 HOUR EMERGENCY SERVICE</span><span>INSTALLATIONS</span><span>REPAIRS</span><span>MAINTENANCE</span><span>COMMERCIAL</span>
  </div>
  <div class="grid">
    <div class="tile tile-feature">
      <h5>MIRUM EST NOSTRE QUAM</h5>
      <p>LOREM IPSUM DOLOR SIT AMET, CONSECTETUR ADIPISCING ELIT NULLA SED</p>
    </div>
    <div class="tile" role="img" aria-label="Project photo of a bright interior with tall glass doors"></div>
    <div class="tile" role="img" aria-label="Project photo of a bright interior with tall glass doors"></div>
    <div class="tile" role="img" aria-label="Project photo of a bright interior with tall glass doors"></div>
    <div class="tile" role="img" aria-label="Project photo of a bright interior with tall glass doors"></div>
    <div class="tile" role="img" aria-label="Project photo of a bright interior with tall glass doors"></div>
    <div class="tile" role="img" aria-label="Project photo of a bright interior with tall glass doors"></div>
    <div class="tile" role="img" aria-label="Project photo of a bright interior with tall glass doors"></div>
  </div>
  <div class="btn-orange">VIEW FULL GALLERY</div>
</section>

<section class="testimonials">
  <div class="testimonials-photo" role="img" aria-label="Background photo of a smiling builder in a hard hat"></div>
  <h2 class="section-title">WHAT OUR CLIENTS SAY</h2>
  <div class="avatar" role="img" aria-label="Client portrait"></div>
  <p class="client">MARIA ELLISON - HOME OWNER</p>
  <p class="quote">"Quick response, tidy work and honest pricing. The team rewired our whole house and fitted new security lights in two days, and they explained every step along the way. We will call them again."</p>
  <div class="dots"><span class="on"></span><span></span><span></span></div>
</section>

<section class="partners">
  <div class="partner"><i></i>LOGO DESIGN</div>
  <div class="partner"><i></i>LOGO DESIGN</div>
  <div class="partner"><i></i>LOGO DESIGN</div>
  <div class="partner"><i></i>LOGO DESIGN</div>
  <div class="partner"><i></i>LOGO DESIGN</div>
</section>

<footer class="site-footer">
  <div class="footer-contact">PH: (555) 014-2290 | FAX: (555) 014-2291<br>EMAIL: INFO@BRIGHTHARBORWIRING.COM</div>
  <div class="footer-brand"><span class="brand-mark"></span><span class="brand-name">Bright Harbor Wiring</span></div>
  <div class="footer-legal">BRIGHTHARBORWIRING <span>| © ALL RIGHTS RESERVED</span></div>
  <div class="footer-social"><span></span><span></span><span></span><span></span></div>
</footer>

</body>
</html>
```